Van wrap for plumbing company on a 2015 hvt corlano.

I am looking to get a van wrap designed. It is for a plumbing company. The van wrap will be on both sides and the back. The logo on all sides. I want it to pop and be attractive. Using the colors of the logo. Must have logo, email, phone number, and website. Id like the colors to be wavy. I like the look of black on top. Dark blue on the bottom with the logo blown up into the background of the blue. With a touch of the lighter blue in there somewhere., Maybe as a stripe in the middle. Id like a view of all sides, driver, passenger, back, nd hood. I want the phone number to be enlarged on all sides.
Target Market(s)
Home owners of all ages and genders
Industry/Entity Type
Plumbing
Requirements
Must have
- Logo. Email. Info@kestrelbend.com phone number (555) 418-6092. Website www.kestrelbend.com
Nice to have
- I would like it to pop and be catchy to the e

```html
<!DOCTYPE html>
<html lang="en">
<head>
<meta charset="utf-8">
<title>Kestrel Bend Plumbing – Vehicle Wraps</title>
<link href="https://fonts.googleapis.com/css2?family=Archivo+Black&display=swap" rel="stylesheet">
<style>
  :root{
    --brand-blue:#1276c0;
    --sky-blue:#7fc3ec;
    --ink:#111111;
    --slate:#58595b;
    --paper:#ffffff;
    --glass:#e4e6e8;
    --tail:#d9262c;
    --trim:#3a3a3a;
  }
  *{margin:0;padding:0;box-sizing:border-box}
  html,body{width:1200px;height:1100px;overflow:hidden;background:var(--paper)}
  body{position:relative;font-family:"Archivo Black",sans-serif}
  .sheet-title{position:absolute;font-size:19px;line-height:30px;letter-spacing:.2px;font-weight:400}
  .sheet-title .series{display:block;color:var(--brand-blue)}
  .sheet-title .model{color:var(--sky-blue)}
  .sheet-title .view{color:var(--slate)}
  .title-side{left:74px;top:28px}
  .title-back{left:704px;top:28px}
  .designer-note{position:absolute;left:642px;top:110px;font-size:12px;line-height:16.5px;color:var(--ink)}
  .van-side{position:absolute;left:30px;width:600px;height:230px}
  .van-side.v1{top:112px}
  .van-side.v2{top:396px}
  .van-side.v3{top:706px}
  .van-back{position:absolute;left:850px;width:260px;height:260px}
  .van-back.v1{top:122px}
  .van-back.v2{top:406px}
  .van-back.v3{top:716px}
  svg text{font-family:"Archivo Black",sans-serif}
</style>
</head>
<body>

<svg width="0" height="0" style="position:absolute" aria-hidden="true">
  <defs>
    <linearGradient id="blueFade" x1="0" y1="0" x2="0" y2="1">
      <stop offset="0" stop-color="#1276c0"/>
      <stop offset="1" stop-color="#8ccbf1"/>
    </linearGradient>
    <clipPath id="sideBody">
      <path d="M18,160 L16,118 Q18,98 50,92 L120,80 L185,24 Q195,14 212,13 L548,8 Q565,8 570,25 L585,100 L586,172 L18,176 Z"/>
    </clipPath>
    <clipPath id="backBody">
      <path d="M22,205 L24,62 Q30,20 72,14 L188,14 Q230,20 236,62 L238,205 Z"/>
    </clipPath>
    <symbol id="wheel" viewBox="-44 -44 88 88">
      <circle r="44" fill="#1b1b1b"/>
      <circle r="40" fill="#2a2a2a"/>
      <circle r="25" fill="#c9cbcd"/>
      <circle r="17" fill="#e6e7e8"/>
      <circle r="7" fill="#555"/>
    </symbol>
    <symbol id="sideChassis" viewBox="0 0 600 230">
      <path d="M18,160 L16,118 Q18,98 50,92 L120,80 L185,24 Q195,14 212,13 L548,8 Q565,8 570,25 L585,100 L586,172 L18,176 Z" fill="none" stroke="var(--trim)" stroke-width="1.5"/>
      <path d="M120,80 L185,24 L200,22 L150,80 Z" fill="#cfd3d6" opacity=".85"/>
      <path d="M152,82 L204,28 L256,26 L256,82 Z" fill="var(--glass)" stroke="#333" stroke-width="2"/>
      <line x1="262" y1="24" x2="264" y2="172" stroke="#333" stroke-width="1"/>
      <line x1="414" y1="20" x2="414" y2="172" stroke="#333" stroke-width="1"/>
      <rect x="8" y="148" width="46" height="22" rx="5" fill="#151515"/>
      <rect x="560" y="156" width="30" height="16" rx="4" fill="#151515"/>
      <rect x="36" y="110" width="14" height="28" rx="3" fill="#2b2b2b"/>
      <rect x="36" y="128" width="14" height="8" fill="#f29a1f"/>
      <rect x="568" y="35" width="9" height="32" rx="3" fill="var(--tail)"/>
      <use href="#wheel" x="51" y="134" width="88" height="88"/>
      <use href="#wheel" x="426" y="134" width="88" height="88"/>
    </symbol>
    <symbol id="backChassis" viewBox="0 0 260 260">
      <path d="M22,205 L24,62 Q30,20 72,14 L188,14 Q230,20 236,62 L238,205" fill="none" stroke="var(--trim)" stroke-width="3"/>
      <rect x="100" y="11" width="60" height="4" rx="2" fill="var(--tail)"/>
      <rect x="12" y="60" width="10" height="42" rx="3" fill="var(--tail)"/>
      <rect x="238" y="60" width="10" height="42" rx="3" fill="var(--tail)"/>
      <rect x="14" y="198" width="232" height="26" rx="7" fill="#151515"/>
      <rect x="24" y="218" width="34" height="36" rx="10" fill="#151515"/>
      <rect x="202" y="218" width="34" height="36" rx="10" fill="#151515"/>
    </symbol>
  </defs>
</svg>

<h1 class="sheet-title title-side"><span class="series">KESTREL BEND VEHICLE WRAPS</span><span class="model">2015 HVT CORLANO</span> <span class="view">SIDE VIEW</span></h1>
<h2 class="sheet-title title-back"><span class="series">KESTREL BEND VEHICLE WRAPS</span><span class="model">2015 HVT CORLANO</span> <span class="view">BACK VIEW</span></h2>

<p class="designer-note">Changes as requested.<br>We can always make some<br>adjustments, Iam flexible.<br>High resolution vector files<br>also ready.</p>

<svg class="van-side v1" viewBox="0 0 600 230" role="group" aria-label="Side view, black and blue wrap">
  <ellipse cx="300" cy="214" rx="290" ry="8" fill="#d6d6d6"/>
  <g clip-path="url(#sideBody)">
    <rect width="600" height="98" fill="var(--ink)"/>
    <rect y="98" width="600" height="5" fill="var(--paper)"/>
    <rect y="103" width="600" height="80" fill="url(#blueFade)"/>
    <rect x="420" y="52" width="145" height="38" fill="var(--paper)" role="img" aria-label="City skyline silhouette with cable bridge"/>
  </g>
  <use href="#sideChassis" width="600" height="230"/>
  <circle cx="340" cy="118" r="60" fill="var(--paper)" stroke="var(--ink)" stroke-width="4"/>
  <text x="340" y="114" text-anchor="middle" font-size="15" fill="var(--ink)"><tspan x="340">KESTREL</tspan><tspan x="340" dy="18">BEND</tspan></text>
  <text x="560" y="44" text-anchor="end" font-size="17" fill="var(--paper)">(555) 418-6092</text>
  <text x="562" y="122" text-anchor="end" font-size="10" fill="var(--paper)">info@kestrelbend.com</text>
  <rect x="420" y="130" width="145" height="15" rx="7.5" fill="var(--brand-blue)"/>
  <text x="492" y="141" text-anchor="middle" font-size="10" fill="var(--paper)">www.kestrelbend.com</text>
</svg>

<svg class="van-side v2" viewBox="0 0 600 230" role="group" aria-label="Side view, blue, white and black wrap">
  <ellipse cx="300" cy="214" rx="290" ry="8" fill="#d6d6d6"/>
  <g clip-path="url(#sideBody)">
    <rect width="600" height="200" fill="var(--brand-blue)"/>
    <path d="M0,150 Q120,100 300,92 L600,80 L600,200 L0,200 Z" fill="var(--paper)"/>
    <path d="M60,200 Q200,130 420,120 L600,118 L600,200 Z" fill="var(--ink)"/>
    <path d="M440,100 Q520,70 600,55 L600,80 Q520,92 440,100 Z" fill="var(--sky-blue)"/>
    <path d="M90,140 Q180,108 260,104 Q180,118 110,150 Z" fill="var(--ink)"/>
    <rect x="420" y="48" width="140" height="38" fill="var(--paper)" role="img" aria-label="City skyline silhouette with cable bridge"/>
  </g>
  <use href="#sideChassis" width="600" height="230"/>
  <circle cx="338" cy="110" r="66" fill="var(--paper)"/>
  <text x="338" y="106" text-anchor="middle" font-size="17" fill="var(--ink)"><tspan x="338">KESTREL</tspan><tspan x="338" dy="20">BEND</tspan></text>
  <text x="560" y="42" text-anchor="end" font-size="17" fill="var(--paper)">(555) 418-6092</text>
  <text x="562" y="114" text-anchor="end" font-size="10" fill="var(--ink)">info@kestrelbend.com</text>
  <text x="562" y="134" text-anchor="end" font-size="10" fill="var(--paper)">www.kestrelbend.com</text>
</svg>

<svg class="van-side v3" viewBox="0 0 600 230" role="group" aria-label="Side view, blue and white wrap">
  <ellipse cx="300" cy="214" rx="290" ry="8" fill="#d6d6d6"/>
  <g clip-path="url(#sideBody)">
    <rect width="600" height="200" fill="var(--paper)"/>
    <path d="M0,0 L600,0 L600,56 Q500,60 430,78 L260,80 Q140,84 0,140 Z" fill="var(--brand-blue)"/>
    <path d="M430,78 Q520,62 600,58 L600,68 Q520,74 430,84 Z" fill="var(--ink)"/>
    <path d="M90,138 Q180,110 240,104 Q180,120 110,148 Z" fill="var(--ink)"/>
    <path d="M440,180 Q450,120 540,108 L600,104 L600,200 L440,200 Z" fill="var(--brand-blue)"/>
    <rect x="420" y="48" width="140" height="34" fill="var(--paper)" role="img" aria-label="City skyline silhouette with cable bridge"/>
  </g>
  <use href="#sideChassis" width="600" height="230"/>
  <circle cx="338" cy="110" r="60" fill="var(--paper)" stroke="var(--ink)" stroke-width="4"/>
  <text x="338" y="106" text-anchor="middle" font-size="15" fill="var(--ink)"><tspan x="338">KESTREL</tspan><tspan x="338" dy="18">BEND</tspan></text>
  <text x="560" y="42" text-anchor="end" font-size="17" fill="var(--paper)">(555) 418-6092</text>
  <text x="562" y="106" text-anchor="end" font-size="10" fill="var(--ink)">info@kestrelbend.com</text>
  <rect x="420" y="113" width="145" height="15" rx="7.5" fill="var(--brand-blue)"/>
  <text x="492" y="124" text-anchor="middle" font-size="10" fill="var(--paper)">www.kestrelbend.com</text>
</svg>

<svg class="van-back v1" viewBox="0 0 260 260" role="group" aria-label="Back view, black and blue wrap">
  <g clip-path="url(#backBody)">
    <rect width="260" height="108" fill="var(--ink)"/>
    <rect y="108" width="260" height="8" fill="var(--paper)"/>
    <rect y="116" width="260" height="100" fill="url(#blueFade)"/>
  </g>
  <use href="#backChassis" width="260" height="260"/>
  <circle cx="130" cy="62" r="40" fill="var(--paper)" stroke="var(--ink)" stroke-width="3"/>
  <text x="130" y="60" text-anchor="middle" font-size="11" fill="var(--ink)"><tspan x="130">KESTREL</tspan><tspan x="130" dy="13">BEND</tspan></text>
  <text x="130" y="140" text-anchor="middle" font-size="17" fill="var(--paper)">(555) 418-6092</text>
  <text x="130" y="158" text-anchor="middle" font-size="10" fill="var(--paper)">info@kestrelbend.com</text>
  <rect x="60" y="164" width="140" height="14" rx="7" fill="var(--brand-blue)"/>
  <text x="130" y="174.5" text-anchor="middle" font-size="9.5" fill="var(--paper)">www.kestrelbend.com</text>
</svg>

<svg class="van-back v2" viewBox="0 0 260 260" role="group" aria-label="Back view, blue, white and black wrap">
  <g clip-path="url(#backBody)">
    <rect width="260" height="216" fill="var(--paper)"/>
    <rect width="260" height="84" fill="var(--brand-blue)"/>
    <rect y="128" width="260" height="62" fill="var(--brand-blue)"/>
    <rect x="150" y="108" width="50" height="18" rx="3" fill="#d5d7d9"/>
    <line x1="130" y1="100" x2="130" y2="128" stroke="#bbb" stroke-width="1"/>
  </g>
  <use href="#backChassis" width="260" height="260"/>
  <circle cx="130" cy="60" r="44" fill="var(--paper)"/>
  <text x="130" y="58" text-anchor="middle" font-size="12" fill="var(--ink)"><tspan x="130">KESTREL</tspan><tspan x="130" dy="14">BEND</tspan></text>
  <text x="130" y="150" text-anchor="middle" font-size="17" fill="var(--paper)">(555) 418-6092</text>
  <text x="130" y="166" text-anchor="middle" font-size="10" fill="var(--paper)">info@kestrelbend.com</text>
  <rect x="60" y="172" width="140" height="14" rx="7" fill="var(--ink)"/>
  <text x="130" y="182.5" text-anchor="middle" font-size="9.5" fill="var(--paper)">www.kestrelbend.com</text>
</svg>

<svg class="van-back v3" viewBox="0 0 260 260" role="group" aria-label="Back view, blue and white wrap">
  <g clip-path="url(#backBody)">
    <rect width="260" height="216" fill="var(--paper)"/>
    <path d="M0,60 Q60,70 90,90 Q130,116 170,90 Q200,70 260,60 L260,100 L0,100 Z" fill="var(--ink)"/>
    <path d="M0,150 Q70,150 80,210 L0,210 Z" fill="var(--brand-blue)"/>
    <path d="M260,150 Q190,150 180,210 L260,210 Z" fill="var(--brand-blue)"/>
    <rect x="150" y="112" width="64" height="26" rx="4" fill="#d5d7d9"/>
    <line x1="130" y1="104" x2="130" y2="150" stroke="#ccc" stroke-width="1"/>
  </g>
  <use href="#backChassis" width="260" height="260"/>
  <circle cx="130" cy="60" r="40" fill="var(--paper)" stroke="var(--ink)" stroke-width="3"/>
  <text x="130" y="58" text-anchor="middle" font-size="11" fill="var(--ink)"><tspan x="130">KESTREL</tspan><tspan x="130" dy="13">BEND</tspan></text>
  <text x="130" y="166" text-anchor="middle" font-size="15" fill="var(--ink)">(555) 418-6092</text>
  <text x="130" y="180" text-anchor="middle" font-size="9.5" fill="var(--brand-blue)">info@kestrelbend.com</text>
  <rect x="62" y="185" width="136" height="13" rx="6.5" fill="var(--brand-blue)"/>
  <text x="130" y="195" text-anchor="middle" font-size="9" fill="var(--paper)">www.kestrelbend.com</text>
</svg>

</body>
</html>
```